Plakat Alternativmedizin
Auftrag sehr gut und passend umgesetzt. Voll getroffen! Und sieht gut aus.
Zielgruppe
Ich bin eine Einzelfirma im Gesundheitswesen und biete Komplementärmedizin an. Die Schwerpunkte liegen auf Akupunktur, Craniosacral Therapie (Form von Osteopathie) und manueller Therapieformen, wie auch klassische Massage.
Aufgabenstellung
Das Plakat ist DIN A1. Das Plakat darf etwas auffallen. Ich habe Komplementär Farben rot und grün.
Der Text: Individuelle Behandlung mit Alternativmedizin.
Mein Name mit DIPL. NATURHEILPRAKTIKERIN, Postadresse und Webseite. Die Angaben sind auf 'Tafel Mauer Gehweg'
Es können auch von Designer gewählte Bilder sein.

```html
<!DOCTYPE html>
<html lang="de">
<head>
<meta charset="utf-8">
<title>Komplementärpraxis – Plakat</title>
<link rel="stylesheet" href="https://fonts.googleapis.com/css2?family=BenchNine:wght@400&family=Tenor+Sans&display=swap">
<style>
  :root {
    --green: #4f8f2c;
    --wine: #6b1230;
    --mauve: #a97d8d;
    --berry: #8c4a65;
    --paper: #ffffff;
    --band-text: #f6eef1;
    --herb: #8fb56f;
    --porcelain: #eeeeec;
    --capsule: #efc85a;
  }
  html, body { margin: 0; padding: 0; overflow: hidden; background: var(--paper); }
  .poster {
    position: relative;
    width: 848px; height: 1200px;
    overflow: hidden;
    background: var(--paper);
    font-family: "Tenor Sans", sans-serif;
  }
  .headline {
    position: absolute; left: 80px; top: 66px; margin: 0;
    font-family: "BenchNine", sans-serif; font-weight: 400;
    font-variant: small-caps;
    font-size: 86px; line-height: 70px;
    letter-spacing: 1px;
    color: var(--green);
  }
  .herbal-photo {
    position: absolute; left: 263px; top: 222px; width: 585px; height: 650px;
    border-radius: 24px 0 0 24px;
    background: linear-gradient(170deg,
      var(--herb) 0%, #c9ddb6 26%, var(--porcelain) 48%,
      #f4f4f2 72%, #f5e3a8 90%, var(--capsule) 100%);
  }
  .services {
    position: absolute; left: 0; top: 540px; margin: 0; padding: 0; list-style: none;
  }
  .services li { position: absolute; white-space: nowrap; line-height: 1; }
  .service-cranio { left: 156px; top: 10px; font-size: 45px; color: var(--mauve); }
  .service-massage { left: 85px; top: 60px; font-size: 58px; color: var(--wine); }
  .service-acu { left: 174px; top: 124px; font-size: 54px; color: var(--berry); }
  .brand-name {
    position: absolute; left: 84px; top: 950px; margin: 0;
    font-size: 32px; color: var(--wine);
    letter-spacing: 1px; line-height: 1;
  }
  .contact-band {
    position: absolute; left: 0; top: 1015px; width: 848px; height: 185px;
    background: var(--wine); color: var(--band-text); text-align: center;
  }
  .contact-name { margin: 0; padding-top: 30px; font-size: 26px; letter-spacing: 3px; }
  .contact-title { margin: 6px 0 0; font-size: 26px; }
  .contact-line { margin: 24px 0 0; font-size: 27px; letter-spacing: 1.5px; }
  .contact-sep { padding: 0 10px; }
</style>
</head>
<body>
<main class="poster">
  <h1 class="headline">Individuelle Behandlung<br>mit Alternativmedizin</h1>

  <div class="herbal-photo" role="img" aria-label="Foto: weisser Mörser mit Stössel, frischen Kräutern und Zimtstange, davor gelbe Kapseln und Tabletten"></div>

  <ul class="services">
    <li class="service-cranio">Craniosacral Therapie</li>
    <li class="service-massage">Massagen</li>
    <li class="service-acu">Akupunktur</li>
  </ul>

  <p class="brand-name">Komplementärpraxis Brunner</p>

  <footer class="contact-band">
    <p class="contact-name">CORNELIA BRUNNER</p>
    <p class="contact-title">Dipl. Naturheilpraktikerin</p>
    <p class="contact-line">079 418 26 37<span class="contact-sep">|</span>www.praxis-brunner.ch</p>
  </footer>
</main>
</body>
</html>
```